Hemp company needs website/online store

We are a startup hemp company and we need an online storefront designed. We are very open do design, but will include our logo to help. We make 100% hemp derived products like edibles, concentrates, vapes and THCA flower. Everything is grown locally, and all products are extracted and made in house.

Requirements
Nice to have
• I would like to highlight that we have Cannabis products that are hemp derived and 100% legal across the US. Also that all cannabis is locally grown and products are extracted and made in house and sent out for third party lab testing.

```html
<!DOCTYPE html>
<html lang="en">
<head>
<meta charset="UTF-8">
<title>Fernrow Hemp</title>
<link href="https://fonts.googleapis.com/css2?family=Poppins:wght@400;500;700&display=swap" rel="stylesheet">
<style>
  :root {
    --green-dark: #3e6f33;
    --green-nav: #3f6a34;
    --white: #ffffff;
    --field-light: #eef4dc;
    --field-mid: #b4d178;
    --field-deep: #6fa23c;
    --field-shadow: #4f8a2c;
  }
  * { box-sizing: border-box; margin: 0; padding: 0; }
  html, body { width: 1200px; height: 669px; overflow: hidden; }
  body { font-family: "Poppins", sans-serif; }

  .hero {
    position: relative;
    width: 1200px;
    height: 669px;
    overflow: hidden;
  }
  .hero-backdrop {
    position: absolute;
    inset: 0;
    background:
      radial-gradient(ellipse 520px 260px at 330px 40px, rgba(248,251,236,0.95), rgba(248,251,236,0) 100%),
      radial-gradient(ellipse 500px 400px at 1050px 420px, rgba(168,201,82,0.7), rgba(168,201,82,0) 100%),
      radial-gradient(ellipse 600px 300px at 200px 669px, rgba(79,138,44,0.85), rgba(79,138,44,0) 100%),
      linear-gradient(180deg, var(--field-light) 0%, var(--field-mid) 45%, var(--field-deep) 85%, var(--field-shadow) 100%);
  }

  .site-header {
    position: absolute;
    top: 0; left: 0; right: 0;
    height: 120px;
  }
  .brand {
    position: absolute;
    left: 83px;
    top: 46px;
    display: flex;
    align-items: center;
    gap: 8px;
    font-weight: 700;
    font-size: 22px;
    color: var(--green-dark);
    letter-spacing: 0.2px;
  }
  .brand-mark {
    width: 14px; height: 14px;
    border-radius: 50%;
    background: var(--green-dark);
  }
  .main-nav {
    position: absolute;
    left: 360px;
    top: 54px;
    display: flex;
    gap: 30px;
  }
  .main-nav a {
    font-weight: 500;
    font-size: 13px;
    color: var(--green-nav);
    text-decoration: none;
  }
  .account-actions {
    position: absolute;
    top: 45px;
    left: 965px;
    display: flex;
    gap: 8px;
  }
  .btn {
    display: inline-flex;
    align-items: center;
    justify-content: center;
    height: 37px;
    border-radius: 3px;
    font-weight: 500;
    font-size: 13px;
    text-decoration: none;
  }
  .btn-outline {
    width: 67px;
    border: 1px solid var(--green-dark);
    color: var(--green-dark);
  }
  .btn-solid {
    width: 76px;
    background: var(--green-dark);
    color: var(--white);
  }

  .hero-content {
    position: absolute;
    left: 81px;
    top: 222px;
    color: var(--white);
  }
  .hero-title {
    font-weight: 700;
    font-size: 40px;
    line-height: 52px;
  }
  .hero-text {
    margin-top: 20px;
    margin-left: 2px;
    font-weight: 400;
    font-size: 13.3px;
    line-height: 20px;
  }
  .hero-cta {
    position: absolute;
    left: 83px;
    top: 488px;
    width: 118px;
    height: 42px;
    background: var(--white);
    color: var(--green-dark);
    font-size: 16px;
    font-weight: 500;
    border-radius: 4px;
  }
</style>
</head>
<body>
  <section class="hero">
    <div class="hero-backdrop" role="img" aria-label="Soft-focus photo of hemp plant leaves in a green field"></div>

    <header class="site-header">
      <div class="brand"><span class="brand-mark"></span>Fernrow Hemp</div>
      <nav class="main-nav">
        <a href="#">HOME</a>
        <a href="#">SERVICES</a>
        <a href="#">PRODUCTS</a>
        <a href="#">ABOUT US</a>
        <a href="#">CONTACT US</a>
      </nav>
      <div class="account-actions">
        <a class="btn btn-outline" href="#">LOG IN</a>
        <a class="btn btn-solid" href="#">SIGN UP</a>
      </div>
    </header>

    <div class="hero-content">
      <h1 class="hero-title">THE LOREM IPSUM<br>DOLOR SIT AMET</h1>
      <p class="hero-text">Lorem Ipsum is simply dummy text of the printing and typesetting industry.<br>Lorem Ipsum has been the industry's standard dummy text</p>
    </div>

    <a class="btn hero-cta" href="#">SIGN UP</a>
  </section>
</body>
</html>
```